Revamp of current landing page for high conversions

I need to revamp my current landing pages and I want to see designs that incorporate elements from both of these current designs... http://www.brightmarlowsmilestudio.com/

https://qrtmno.pagewick.co/vorn-glowpackoffer77/

Please implement these images into the design: https://www.pictogram.example/p/KQX7Lm2R_Ta-/?taken-by=brightmarlowsmilestudio

https://www.pictogram.example/p/KR4WnsJdpzG/?taken-by=brightmarlowsmilestudio

https://www.pictogram.example/p/KRvqDmtk9_P/?taken-by=brightmarlowsmilestudio

https://www.pictogram.example/p/KRjemTGkRVN/?taken-by=brightmarlowsmilestudio

https://www.pictogram.example/p/KRjfa93kd-d/?taken-by=brightmarlowsmilestudio

https://www.pictogram.example/p/KReZoGTEuHa/?taken-by=brightmarlowsmilestudio

https://www.pictogram.example/p/KRThd5hkmc9/?taken-by=brightmarlowsmilestudio

https://www.pictogram.example/p/KRBksT0EcSu/?taken-by=brightmarlowsmilestudio

https://www.pictogram.example/p/KS8h5SjE8H9/?taken-by=brightmarlowsmilestudio

Target Market(s)

People that care about their looks and who want whiter teeth. People that are interested in good oral hygeine

Industry/Entity Type

Dental Clinic

Number of Pages Required

1 page

Colors

Designer to choose colors to be used in the design.

Requirements
Must have
• images of my customers that I have included in the description.
• Also, I would like to see a professional laser teeth whitening treatment that happens in dental office and make emphasis on FREE HOME MAINTENANCE KIT INCLUDED!
• Must have CALL OR TEXT 555-014-3827
Nice to have
• Must be mobile friendly responsive design-use logo from my website www.brightmarlowsmilestudo.com
Should not have
• stock images of people I dont like stock images of people so please use the images from my instagram account

```html
<!DOCTYPE html>
<html lang="en">
<head>
<meta charset="utf-8">
<title>Bright Marlow Smile Studio – $99 Teeth Whitening</title>
<link href="https://fonts.googleapis.com/css2?family=Lora:ital,wght@0,400;0,600;0,700;1,400&family=Roboto:wght@400;500;700&display=swap" rel="stylesheet">
<style>
:root{
  --navy:#0d3b6b;
  --navy-deep:#0a2547;
  --sky:#6ec8f2;
  --sky-pale:#eaf5fc;
  --coral:#f2544f;
  --gold:#fcc96a;
  --gold-text:#f9c86b;
  --star:#f4b63f;
  --ink:#2b2b2b;
  --white:#fff;
  --row-alt:#efefef;
}
*{box-sizing:border-box;margin:0;padding:0}
html,body{width:1200px;height:2273px;overflow:hidden;background:var(--white)}
body{position:relative;font-family:'Roboto',Arial,sans-serif;color:var(--ink)}

/* header */
.site-header{position:absolute;left:0;top:0;width:1200px;height:115px}
.brand{position:absolute;left:110px;top:24px;display:flex;align-items:center;gap:12px}
.brand-dot{width:64px;height:64px;border-radius:50%;background:#dfe3e8}
.brand-name{font-family:'Lora',Georgia,serif;font-weight:600;font-size:25px;line-height:1.05;color:var(--navy)}
.header-contact{position:absolute;right:112px;top:22px;text-align:right}
.header-contact .label{font-size:15px;color:#444}
.header-contact .phone{font-family:'Lora',Georgia,serif;font-size:27px;color:var(--sky);font-weight:600;line-height:1.2}
.header-contact .where{font-size:15px;color:#444;margin-top:4px}

/* hero */
.hero{position:absolute;left:0;top:115px;width:1200px;height:600px;overflow:hidden}
.hero-photo{position:absolute;inset:0;background:linear-gradient(100deg,#3b1c4a 0%,#6a2f7d 30%,#5a3cc0 55%,#3d2a62 80%,#2a2434 100%)}
.hero-title{position:absolute;left:105px;top:62px;font-family:'Lora',Georgia,serif;font-weight:700;color:var(--white);font-size:33px;line-height:1.07;text-align:center;width:430px}
.hero-price{position:absolute;left:540px;top:52px;font-family:'Lora',Georgia,serif;font-weight:700;color:var(--gold-text);font-size:76px;line-height:1}
.hero-price sup{font-size:44px;vertical-align:top;position:relative;top:6px}
.benefits{position:absolute;left:110px;top:168px;list-style:none}
.benefits li{display:flex;align-items:center;gap:10px;color:var(--white);font-size:16px;height:29px}
.benefits svg{width:14px;height:14px}
.kit-photo{position:absolute;left:118px;top:380px;width:250px;height:160px;border-radius:10px;background:linear-gradient(135deg,#c9d4ea,#eef1f7 50%,#9fb0d6);opacity:.85}
.includes{position:absolute;left:452px;top:328px;width:226px;height:226px;border-radius:50%;background:var(--coral);box-shadow:0 0 0 10px rgba(255,255,255,.18);color:var(--white);text-align:center;padding-top:50px;font-size:15.5px;line-height:1.45;z-index:2}
.includes strong{display:block;font-weight:700;margin-bottom:8px;font-size:16px}

.coupon{position:absolute;left:780px;top:40px;width:308px;height:440px;background:var(--white);box-shadow:0 4px 12px rgba(0,0,0,.3)}
.coupon-head{position:relative;height:135px;color:var(--white);text-align:center;padding-top:18px}
.coupon-head svg{position:absolute;left:0;top:0;width:308px;height:135px;z-index:0}
.coupon-head .pre,.coupon-head h2{position:relative;z-index:1}
.coupon-head .pre{font-size:14.5px;font-weight:700}
.coupon-head .pre span{color:var(--sky)}
.coupon-head h2{font-family:'Lora',Georgia,serif;font-weight:700;font-size:23px;line-height:1.05;margin-top:4px}
.coupon-form{padding:14px 26px 0}
.field{height:34px;border:1px solid #cfe3f1;background:var(--sky-pale);margin-bottom:9px;font-size:13px;color:#8a9aa6;padding:9px 12px}
.cta{height:34px;background:var(--navy);color:var(--white);font-weight:700;font-size:15px;text-align:center;line-height:34px;margin-top:2px}
.coupon-foot{position:absolute;left:0;bottom:0;width:308px;height:94px;background:var(--gold);text-align:center;padding-top:16px;font-size:15px;font-weight:500;line-height:1.3;color:#1f1f1f}
.coupon-foot::before{content:"";position:absolute;left:144px;top:-10px;border:10px solid transparent;border-top-color:var(--white);border-bottom:0}
.badge{display:inline-block;background:var(--coral);color:var(--white);font-size:10.5px;font-weight:700;border-radius:12px;padding:3px 14px;margin-bottom:6px}
.hero-wave{position:absolute;left:0;top:490px;width:1200px;height:110px;z-index:1}

/* intro */
.intro{position:absolute;left:195px;top:748px;width:810px;text-align:center;font-family:'Lora',Georgia,serif;font-style:italic;font-size:22px;line-height:1.4;color:#333}

/* how it works */
.how{position:absolute;left:110px;top:876px;width:978px;height:268px;border:1px solid #e4e8ee;border-radius:6px;background:#fdfcf8;overflow:hidden}
.how-team{position:absolute;left:0;top:0;width:420px;height:268px;background:linear-gradient(135deg,#efe9e4,#d7c9c4 45%,#9c4a5e 75%,#e7ddd8)}
.how-smile{position:absolute;right:0;top:0;width:180px;height:268px;background:linear-gradient(160deg,#e8c08a,#f3e3d4 50%,#e6b6a1)}
.how-copy{position:absolute;left:430px;top:44px;width:360px;padding:0 10px;text-align:center}
.how-copy h2{font-family:'Lora',Georgia,serif;color:var(--navy);font-size:23px;font-weight:700;margin-bottom:16px}
.how-copy p{font-size:15px;line-height:1.52;color:#444}

/* reviews */
.reviews{position:absolute;left:110px;top:1208px;width:560px}
.reviews h2{font-family:'Lora',Georgia,serif;color:var(--navy);font-size:23px;font-weight:700}
.reviews .rated{font-size:14.5px;font-weight:500;color:#444;margin-top:2px}
.review-source{margin-top:38px;font-weight:700;font-size:20px;color:#222}
.stars{display:flex;gap:3px;margin-top:4px}
.stars svg{width:20px;height:20px}
.quote{margin-top:22px;font-size:15.5px;line-height:1.5;color:#333}
.author{margin-top:18px;font-size:15px;font-weight:700;color:#444}

.promo{position:absolute;left:780px;top:1215px;width:308px;height:376px;background:var(--gold);border-radius:6px;overflow:hidden;text-align:center}
.promo h3{font-family:'Lora',Georgia,serif;font-weight:700;color:var(--navy);font-size:23px;line-height:1.05;margin-top:20px}
.promo-circle{position:absolute;left:72px;top:102px;width:166px;height:166px;border-radius:50%;background:var(--coral);color:var(--white)}
.promo-circle .for{font-family:'Lora',Georgia,serif;font-style:italic;font-size:16px;margin-top:20px}
.promo-circle .amt{font-family:'Lora',Georgia,serif;font-weight:700;font-size:72px;line-height:1}
.promo-circle .amt sup{font-size:38px;vertical-align:top;position:relative;top:6px}
.promo-bar{position:absolute;left:0;top:214px;width:308px;height:58px;background:#000;color:var(--white);font-family:'Lora',Georgia,serif;font-weight:700;font-size:14px;line-height:1.3;padding-top:11px}
.promo-foot{position:absolute;left:24px;top:286px;width:260px}
.promo-foot strong{display:block;font-size:15px;color:#111;margin-bottom:4px}
.promo-foot p{font-size:13px;line-height:1.35;color:#222}

/* compare */
.compare-title{position:absolute;left:0;top:1652px;width:1200px;text-align:center;font-family:'Lora',Georgia,serif;font-weight:700;font-size:23px;color:var(--navy)}
.compare{position:absolute;left:110px;top:1710px;width:978px;height:306px;border:1px solid #e2e6ea;background:var(--white);padding:9px}
.compare table{width:958px;border-collapse:collapse;table-layout:fixed}
.compare th{height:68px;background:var(--sky);color:var(--white);font-family:'Lora',Georgia,serif;font-weight:600;font-size:20px;border-right:2px solid var(--white)}
.compare th.us{background:var(--navy)}
.us-mark{display:inline-flex;align-items:center;gap:6px;font-family:'Lora',Georgia,serif;font-weight:600;font-size:13px;line-height:1.05;color:var(--white);text-align:left}
.us-mark i{width:28px;height:28px;border-radius:50%;background:#dfe3e8;display:block}
.compare td{height:44px;text-align:center;font-size:13.5px;color:#444;border-right:2px solid var(--white)}
.compare td:first-child{font-size:15px;font-weight:500;color:#222}
.compare tr:nth-child(odd) td{background:var(--row-alt)}
.compare tr:nth-child(even) td{background:#f8f8f8}

/* footer */
.footer-wave{position:absolute;left:0;top:2040px;width:1200px;height:100px}
.site-footer{position:absolute;left:0;top:2118px;width:1200px;height:155px;background:var(--navy-deep);color:var(--white);text-align:center}
.footer-dot{position:absolute;left:568px;top:2074px;width:64px;height:64px;border-radius:50%;background:#dfe3e8;border:3px solid var(--white)}
.site-footer .label{margin-top:50px;font-size:15px}
.site-footer .phone{font-family:'Lora',Georgia,serif;font-size:26px;color:var(--sky);font-weight:600;line-height:1.2}
.site-footer .copy{margin-top:16px;font-size:12.5px}
</style>
</head>
<body>

<header class="site-header">
  <div class="brand">
    <span class="brand-dot"></span>
    <span class="brand-name">Bright Marlow's<br>Smile Studio</span>
  </div>
  <div class="header-contact">
    <div class="label">Call or Text to Book</div>
    <div class="phone">555-014-3827</div>
    <div class="where">Conveniently Located In Harbor Flats</div>
  </div>
</header>

<section class="hero">
  <div class="hero-photo" role="img" aria-label="Client reclining in a dental chair during a blue light whitening treatment"></div>
  <h1 class="hero-title">$378 TEETH WHITENING SYSTEM FOR ONLY</h1>
  <div class="hero-price"><sup>$</sup>99</div>
  <ul class="benefits">
    <li><svg viewBox="0 0 14 14"><rect width="14" height="14" rx="2" fill="#fcc96a"/><path d="M3 7.5l2.6 2.6L11 4.5" stroke="#3b1c4a" stroke-width="2" fill="none"/></svg>No Pain - No Sensitivity</li>
    <li><svg viewBox="0 0 14 14"><rect width="14" height="14" rx="2" fill="#fcc96a"/><path d="M3 7.5l2.6 2.6L11 4.5" stroke="#3b1c4a" stroke-width="2" fill="none"/></svg>Cosmetic Procedure</li>
    <li><svg viewBox="0 0 14 14"><rect width="14" height="14" rx="2" fill="#fcc96a"/><path d="M3 7.5l2.6 2.6L11 4.5" stroke="#3b1c4a" stroke-width="2" fill="none"/></svg>Results Less Than An Hour</li>
    <li><svg viewBox="0 0 14 14"><rect width="14" height="14" rx="2" fill="#fcc96a"/><path d="M3 7.5l2.6 2.6L11 4.5" stroke="#3b1c4a" stroke-width="2" fill="none"/></svg>Blue Laser Technology</li>
    <li><svg viewBox="0 0 14 14"><rect width="14" height="14" rx="2" fill="#fcc96a"/><path d="M3 7.5l2.6 2.6L11 4.5" stroke="#3b1c4a" stroke-width="2" fill="none"/></svg>2-8 Shades Lighter</li>
    <li><svg viewBox="0 0 14 14"><rect width="14" height="14" rx="2" fill="#fcc96a"/><path d="M3 7.5l2.6 2.6L11 4.5" stroke="#3b1c4a" stroke-width="2" fill="none"/></svg>Convenient Location in Marlow Bay</li>
  </ul>
  <div class="kit-photo" role="img" aria-label="Home maintenance kit with whitening gel syringes and mouth tray"></div>
  <div class="includes"><strong>INCLUDES:</strong>1 In Office Teeth<br>Whitening Treatment<br>45 Minutes and<br>1 Free Home<br>Maintenance Kit</div>

  <aside class="coupon">
    <div class="coupon-head">
      <svg viewBox="0 0 308 135" preserveAspectRatio="none"><path d="M0 0H308V118Q230 96 154 118T0 112Z" fill="#0d3b6b"/></svg>
      <div class="pre">Enter Your Info To Be Emailed The <span>$99</span></div>
      <h2>TEETH WHITENING<br>COUPON</h2>
    </div>
    <div class="coupon-form">
      <div class="field">Name</div>
      <div class="field">Email</div>
      <div class="field">Phone</div>
      <div class="cta">GET A DEAL!</div>
    </div>
    <div class="coupon-foot">
      <span class="badge">LIMITED TIME OFFER</span><br>
      Limited Appointments Available<br>Print Free Coupon
    </div>
  </aside>
  <svg class="hero-wave" viewBox="0 0 1200 110" preserveAspectRatio="none">
    <path d="M0 52Q260 36 520 66T1200 28V110H0Z" fill="#6ec8f2"/>
    <path d="M0 40Q250 30 520 70T1200 78V110H0Z" fill="#0d3b6b"/>
    <path d="M0 64Q260 46 540 86T1200 90V110H0Z" fill="#fff"/>
  </svg>
</section>

<p class="intro">Why pay hundreds of dollars when you can get a professional teeth whitening procedure for much less than your local dentist office?</p>

<section class="how">
  <div class="how-team" role="img" aria-label="Studio team with a client holding a My First Whitening sign"></div>
  <div class="how-copy">
    <h2>HOW IT WORKS:</h2>
    <p>We utilize the latest Blue Light Whitening Technology in combination with our Hydrogen Peroxide Whitening Gel to accelerate the whitening process! It's effective, safe and affordable! With our treatment your smile will be noticeably whiter in less than an hour!</p>
  </div>
  <div class="how-smile" role="img" aria-label="Client smiling after whitening"></div>
</section>

<section class="reviews">
  <h2>WHAT OUR CLIENTS SAY</h2>
  <div class="rated">Excellent 5 Star Rated on Revuely.com</div>
  <div class="review-source">Revuely</div>
  <div class="stars" aria-label="5 out of 5 stars">
    <svg viewBox="0 0 12 12"><path d="M6 .6l1.6 3.4 3.7.4-2.8 2.5.8 3.7L6 8.7 2.7 10.6l.8-3.7L.7 4.4l3.7-.4z" fill="#f4b63f"/></svg>
    <svg viewBox="0 0 12 12"><path d="M6 .6l1.6 3.4 3.7.4-2.8 2.5.8 3.7L6 8.7 2.7 10.6l.8-3.7L.7 4.4l3.7-.4z" fill="#f4b63f"/></svg>
    <svg viewBox="0 0 12 12"><path d="M6 .6l1.6 3.4 3.7.4-2.8 2.5.8 3.7L6 8.7 2.7 10.6l.8-3.7L.7 4.4l3.7-.4z" fill="#f4b63f"/></svg>
    <svg viewBox="0 0 12 12"><path d="M6 .6l1.6 3.4 3.7.4-2.8 2.5.8 3.7L6 8.7 2.7 10.6l.8-3.7L.7 4.4l3.7-.4z" fill="#f4b63f"/></svg>
    <svg viewBox="0 0 12 12"><path d="M6 .6l1.6 3.4 3.7.4-2.8 2.5.8 3.7L6 8.7 2.7 10.6l.8-3.7L.7 4.4l3.7-.4z" fill="#f4b63f"/></svg>
  </div>
  <p class="quote">“So I just had my teeth whitened using the blue laser light and I have to say this was one of the best experiences I've had with teeth whitening. Marisol (the women who helped me) was very clear about the process and walked me through each ste. I would say the whole process took about 45-60 minutes. After the teeth whitening process was finished I could tell immediately and I was very pleased with the end results.”</p>
  <div class="author">- Dario M. Marlow Bay</div>
</section>

<aside class="promo">
  <h3>AFFORDABLE<br>TEETH WHITENING<br>IN MARLOW BAY</h3>
  <div class="promo-circle">
    <div class="for">for only</div>
    <div class="amt"><sup>$</sup>99</div>
  </div>
  <div class="promo-bar">SAVE HUNDREDS VS GOING TO<br>YOUR LOCAL DENTIST!</div>
  <div class="promo-foot">
    <strong>The best price, service and results</strong>
    <p>Get ready for High School Prom, Mother's Day, Graduation, Wedding, Vacation, or any Occasion.</p>
  </div>
</aside>

<h2 class="compare-title">COMPARE US</h2>
<section class="compare">
  <table>
    <thead>
      <tr>
        <th>FEATURES</th>
        <th class="us"><span class="us-mark"><i></i>Bright Marlow's<br>Smile Studio</span></th>
        <th>LUMINA</th>
        <th>GLOW PRO</th>
        <th>OTHER</th>
      </tr>
    </thead>
    <tbody>
      <tr><td>Speed</td><td>Results in 45 minutes</td><td>Results in 3 Treatments</td><td>Results in 1 Hour</td><td>7-10 Days</td></tr>
      <tr><td>Ease of Use</td><td>Very Easy</td><td>Difficult/Dentist</td><td>Difficult/Dentist</td><td>Self</td></tr>
      <tr><td>Cost</td><td>$378</td><td>$600-$1000</td><td>$399-$600</td><td>$50-$150</td></tr>
      <tr><td>Time Requirements</td><td>Less Than An Hour</td><td>3 Hours</td><td>1 Hour + Home Treatment</td><td>Nightly 7-30 Days</td></tr>
      <tr><td>Availability</td><td>Walk-In &amp; By Appt</td><td>By Appointment Only</td><td>By Appointment Only</td><td>Store Purchas</td></tr>
    </tbody>
  </table>
</section>

<svg class="footer-wave" viewBox="0 0 1200 100" preserveAspectRatio="none">
  <path d="M0 50Q300 10 600 48T1200 10V100H0Z" fill="#6ec8f2"/>
  <path d="M0 60Q300 35 600 70T1200 40V100H0Z" fill="#fff"/>
  <path d="M0 66Q320 46 620 80T1200 30V100H0Z" fill="#0a2547"/>
</svg>
<footer class="site-footer">
  <div class="label">Call or Text to Book</div>
  <div class="phone">555-014-3827</div>
  <div class="copy">Copyright © 2017 Bright Marlow Smile Studio</div>
</footer>
<span class="footer-dot"></span>

</body>
</html>
```